Label designs for three different cider varieties

The Larkmoor Perry Works is a family run business. We have been making cider within the family as a hobby for over 100 years and we have recently decided to start to try to sell the cider. Therefore this project is to create a logo and three product labels for three different varieties of cider. So we should end up with four files; one for the logo and one for each of the labels. The files need to be in an editable format for us so that we can add edit the batch numbers e.g. PNG file.
For the logo we would like to use the Pellow Family Shield since Pellow is our family name. We would like it adapted into a cider themed crest, for example with apples and trees. We are open to ideas about the logo but this is just our initial idea. Example of the original Pellow Family Shield can be seen in the link below:
http://www.vinshadeheraldry.net/arms/Pellow-England.jpg
The labels should be no bigger than 93mm in height and 213mm in length. Each label should be similar in style so it is clear the three different varieties of cider are from the same company. Each label must have the following information since this is a legal requirement:
- The logo you have created
- The Larkmoor Perry Works Ltd.
- 52 Mirefield Row, Taunton, Somerset, TA4 9QX
- Alcohol: 6% vol
- 500ml
- Allergens: Contains Sulphites for freshness
- There needs to be space on the label for batch numbers. This is four numbers e.g. 1701.
- Family craft cider makers using only premium apples from our own traditional Somerset orchard.
The names of the three cider varieties are:
- Larkmoor Heritage
- Larkmoor Amber
- Larkmoor Kingsbury
Our initial idea is that each variety would have its own colour associated with it; i.e. black themed label for Larkmoor Heritage, gold themed label for Larkmoor Amber and a red themed label for Larkmoor Kingsbury. The crest logo you have created would then be in the themed colour for that cider variety i.e. black, gold or red.
We would like the labels to reflect the following themes for our brand:
- High end premium brand
- Clean and simple design
- Modern
Overall we are very open to ideas and we do not want to constrain your creativity. All of the above is just our initial ideas but we would love to see what ideas you have. The only things that cannot change are what must be on the label since this is a legal requirement we have to meet.

```html
<!DOCTYPE html>
<html lang="en">
<head>
<meta charset="utf-8">
<title>The Larkmoor Perry Works – Cider Labels</title>
<link rel="stylesheet" href="https://fonts.googleapis.com/css2?family=Bebas+Neue&family=Playfair+Display:ital,wght@0,700;1,400&family=Roboto+Condensed:wght@300;400;700&display=swap">
<style>
:root{
  --panel:#3d3d3f;
  --stage:#e9e9e9;
  --label-black:#1b1b1c;
  --label-black-2:#2a2a2b;
  --gold:#c9a24a;
  --gold-light:#e6c77a;
  --silver:#d9d9d9;
  --red:#d3141d;
  --red-dark:#8e0c10;
  --white:#ffffff;
  --text-soft:#bdbdbd;
  --rule:#b8923c;
}
*{box-sizing:border-box;margin:0;padding:0}
html,body{width:1200px;height:710px;overflow:hidden}
body{background:var(--stage);font-family:"Roboto Condensed",Arial,sans-serif;position:relative}

/* Brand mark panel */
.brand-panel{position:absolute;left:0;top:0;width:168px;height:710px;background:var(--panel);
  display:flex;flex-direction:column;justify-content:space-around;align-items:center;padding:20px 0}
.brand-mark{display:flex;flex-direction:column;align-items:center;gap:10px;width:130px;text-align:center}
.brand-mark .dot{width:34px;height:34px;border-radius:50%;background:currentColor}
.brand-mark .name{font-family:"Playfair Display",Georgia,serif;font-weight:700;font-size:21px;line-height:1.05}
.brand-mark.gold{color:var(--gold)}
.brand-mark.white{color:var(--white)}

/* Label row */
.label-row{position:absolute;left:168px;top:0;width:1032px;height:710px;
  display:flex;justify-content:space-evenly;align-items:flex-start;padding-top:70px}
.label-set{width:236px;display:flex;flex-direction:column;align-items:center;gap:44px}

.neck-band{width:132px;height:86px;background:linear-gradient(180deg,#0f0f10,#262627 50%,#0f0f10);
  display:flex;align-items:center;justify-content:center}
.neck-band.red{background:linear-gradient(180deg,var(--red-dark),#c1141b 50%,var(--red-dark))}
.neck-band.gold{background:repeating-linear-gradient(180deg,#e3c680 0 2px,#d8b765 2px 4px)}
.neck-band .mini-mark{display:flex;flex-direction:column;align-items:center;gap:3px;color:var(--gold);width:70px;text-align:center}
.neck-band.gold .mini-mark{color:#8a6a25}
.neck-band.red .mini-mark{color:var(--gold-light)}
.mini-mark .dot{width:12px;height:12px;border-radius:50%;background:currentColor}
.mini-mark .name{font-family:"Playfair Display",Georgia,serif;font-weight:700;font-size:9.5px;line-height:1.05}

.body-label{position:relative;width:236px;height:312px;
  background:linear-gradient(180deg,var(--label-black-2),var(--label-black) 40%,var(--label-black-2));
  border-top:3px solid var(--rule);border-bottom:3px solid var(--rule);color:var(--text-soft);
  display:flex;flex-direction:column;align-items:center;padding:10px 12px 8px}
.body-label::before,.body-label::after{content:"";position:absolute;left:0;right:0;height:1px;background:var(--rule);opacity:.7}
.body-label::before{top:4px}
.body-label::after{bottom:4px}

.label-mark{display:flex;flex-direction:column;align-items:center;gap:4px;color:var(--gold);width:92px;text-align:center;z-index:1}
.label-mark .dot{width:22px;height:22px;border-radius:50%;background:currentColor}
.label-mark .name{font-family:"Playfair Display",Georgia,serif;font-weight:700;font-size:13px;line-height:1.05}

.apple-art{position:absolute;left:50%;top:66px;transform:translateX(-50%);width:120px;height:120px;border-radius:50%;
  background:radial-gradient(circle,rgba(255,255,255,.08),rgba(255,255,255,0) 70%)}
.red-theme .apple-art{background:radial-gradient(circle,rgba(211,20,29,.35),rgba(211,20,29,0) 70%)}

.variety-name{font-family:"Bebas Neue",Impact,sans-serif;font-size:42px;line-height:.86;text-align:center;
  margin-top:14px;letter-spacing:.5px;z-index:1;color:var(--silver)}
.red-theme .variety-name{color:var(--red)}
.gold-theme .variety-name{color:var(--gold-light)}
.variety-style{font-family:"Playfair Display",Georgia,serif;font-style:italic;font-size:12px;color:var(--gold);margin-top:4px;z-index:1}
.red-theme .variety-style,.gold-theme .variety-style{color:#e0e0e0}
.flourish{width:70px;height:1px;background:var(--rule);margin-top:6px}

.info-row{margin-top:auto;width:100%;display:flex;align-items:stretch;border-top:1px solid rgba(201,162,74,.5);padding-top:6px;margin-bottom:4px}
.info-volume{width:48px;display:flex;flex-direction:column;justify-content:space-between;align-items:center;
  font-size:9px;text-transform:uppercase;line-height:1.15;text-align:center;border-right:1px solid rgba(201,162,74,.5);padding-right:6px}
.info-volume hr{border:0;border-top:1px solid rgba(201,162,74,.5);width:100%;margin:4px 0}
.info-claim{flex:1;font-size:8.6px;text-transform:uppercase;text-align:center;line-height:1.3;padding:0 6px;
  border-right:1px solid rgba(201,162,74,.5)}
.tree-art{width:40px;display:flex;align-items:center;justify-content:center}
.tree-art span{display:block;width:26px;height:40px;border-radius:13px 13px 3px 3px;background:linear-gradient(180deg,rgba(255,255,255,.7),rgba(255,255,255,.25))}

/* Back label */
.back-label{align-items:stretch;padding:10px 12px 8px}
.back-head{display:flex;justify-content:space-between;align-items:flex-start}
.back-title{font-family:"Bebas Neue",Impact,sans-serif;font-size:27px;line-height:.86;color:var(--silver)}
.back-address{font-size:6.2px;text-transform:uppercase;line-height:1.3;margin-top:4px;color:var(--text-soft)}
.back-head .label-mark{width:70px}
.back-head .label-mark .name{font-size:10px}
.back-head .label-mark .dot{width:16px;height:16px}
.back-info{display:flex;align-items:stretch;margin-top:8px;border-top:1px solid rgba(201,162,74,.5);border-bottom:1px solid rgba(201,162,74,.5);padding:5px 0}
.back-info .info-claim{font-size:7.4px}
.batch{font-size:6.5px;text-transform:uppercase;display:flex;flex-direction:column;justify-content:flex-end;align-items:center;width:52px;gap:4px}
.batch .tree-art span{width:18px;height:28px}
.allergens{font-size:8.5px;text-transform:uppercase;text-align:center;margin:6px 0 5px;color:#e0e0e0;font-weight:700}
.back-copy{font-size:6.9px;line-height:1.35;color:var(--text-soft);margin-bottom:5px}
</style>
</head>
<body>

<aside class="brand-panel">
  <div class="brand-mark gold"><span class="dot"></span><span class="name">The Larkmoor Perry Works</span></div>
  <div class="brand-mark gold"><span class="dot"></span><span class="name">The Larkmoor Perry Works</span></div>
  <div class="brand-mark white"><span class="dot"></span><span class="name">The Larkmoor Perry Works</span></div>
</aside>

<main class="label-row">

  <!-- Heritage front -->
  <section class="label-set">
    <div class="neck-band"><div class="mini-mark"><span class="dot"></span><span class="name">The Larkmoor Perry Works</span></div></div>
    <div class="body-label">
      <div class="apple-art" role="img" aria-label="Faint engraved apple illustration"></div>
      <div class="label-mark"><span class="dot"></span><span class="name">The Larkmoor Perry Works</span></div>
      <h2 class="variety-name">Larkmoor<br>Heritage</h2>
      <p class="variety-style">Dry Cyder</p>
      <span class="flourish"></span>
      <div class="info-row">
        <div class="info-volume"><span>Alc vol:<br>6%</span><hr><span>500ml</span></div>
        <p class="info-claim">Family craft cider makers using only premium apples from our own traditional Somerset orchard.</p>
        <div class="tree-art" role="img" aria-label="Apple tree illustration"><span></span></div>
      </div>
    </div>
  </section>

  <!-- Heritage back -->
  <section class="label-set">
    <div class="neck-band"><div class="mini-mark"><span class="dot"></span><span class="name">The Larkmoor Perry Works</span></div></div>
    <div class="body-label back-label">
      <div class="back-head">
        <div>
          <h2 class="back-title">Larkmoor<br>Heritage</h2>
          <p class="back-address">The Larkmoor Perry Works Ltd.<br>52 Mirefield Row, Taunton, Somerset, TA4 9QX</p>
        </div>
        <div class="label-mark"><span class="dot"></span><span class="name">The Larkmoor Perry Works</span></div>
      </div>
      <div class="back-info">
        <div class="info-volume"><span>Alc vol:<br>6%</span><hr><span>500ml</span></div>
        <p class="info-claim">Family craft cider makers using only premium apples from our own traditional Somerset orchard.</p>
        <div class="batch"><div class="tree-art" role="img" aria-label="Apple tree illustration"><span></span></div><span>Batch number: 1701</span></div>
      </div>
      <p class="allergens">Allergens: contains sulphites for freshness</p>
      <p class="back-copy">A crisp and refreshing cider, its fresh apple aroma and slightly sweet, ripe apple flavours make it hard to resist.</p>
      <p class="back-copy">Developed to be the perfect balance of sweetness and dry acidity, a wonderful blended cider for the cider lover or newcomer alike. Made entirely from the fermentation of apple juice picked by hand in our own orchard.</p>
    </div>
  </section>

  <!-- Kingsbury front -->
  <section class="label-set red-theme">
    <div class="neck-band red"><div class="mini-mark"><span class="dot"></span><span class="name">The Larkmoor Perry Works</span></div></div>
    <div class="body-label">
      <div class="apple-art" role="img" aria-label="Red engraved apple illustration"></div>
      <div class="label-mark"><span class="dot"></span><span class="name">The Larkmoor Perry Works</span></div>
      <h2 class="variety-name">Larkmoor<br>Kingsbury</h2>
      <p class="variety-style">Single Variety Cyder</p>
      <span class="flourish"></span>
      <div class="info-row">
        <div class="info-volume"><span>Alc vol:<br>6%</span><hr><span>500ml</span></div>
        <p class="info-claim">Family craft cider makers using only premium apples from our own traditional Somerset orchard.</p>
        <div class="tree-art" role="img" aria-label="Apple tree illustration"><span></span></div>
      </div>
    </div>
  </section>

  <!-- Amber front -->
  <section class="label-set gold-theme">
    <div class="neck-band gold"><div class="mini-mark"><span class="dot"></span><span class="name">The Larkmoor Perry Works</span></div></div>
    <div class="body-label">
      <div class="apple-art" role="img" aria-label="Faint engraved apple illustration"></div>
      <div class="label-mark"><span class="dot"></span><span class="name">The Larkmoor Perry Works</span></div>
      <h2 class="variety-name">Larkmoor<br>Amber</h2>
      <p class="variety-style">Medium Dry Cyder</p>
      <span class="flourish"></span>
      <div class="info-row">
        <div class="info-volume"><span>Alc vol:<br>6%</span><hr><span>500ml</span></div>
        <p class="info-claim">Family craft cider makers using only premium apples from our own traditional Somerset orchard.</p>
        <div class="tree-art" role="img" aria-label="Apple tree illustration"><span></span></div>
      </div>
    </div>
  </section>

</main>
</body>
</html>
```